Business Card & Stationary Design Project

We are looking for some creative direction for business cards and our stationary.

We are a global logistics firm that has recently changed its name to Marrick Global Logistics and we have a new website due out tomorrow (www.marrick.com.au).

The colours of the company are rich navy tones, I would like to have business cards that fit together to make one picture on the back (possibly an old map of the world??), and the front to be modern contemporary looking.

But I am open to suggestions, so just incorporate our new logo and get going!
Updates

Hi Everyone,

Thank you for all of your designs so far and the time you have put into it.

I have asked many of you for amendments to see if we can get a final product, so with this in mind I am extending the deadline by a few days.

Good luck and thank you once again.

Please message me direct if you need any clarification.

Kind Regards
Colin

Reason: As outlined the extra 3 days is for amendments and changes to the current submissions. Thanks Colin

Industry/Entity Type

Business

```html
<!DOCTYPE html>
<html lang="en">
<head>
<meta charset="utf-8">
<title>Marrick Global Logistics – Mailing Labels</title>
<link rel="stylesheet" href="https://fonts.googleapis.com/css2?family=Questrial&display=swap">
<style>
  :root {
    --backdrop: #3b3b3b;
    --label-paper: #e7e7e7;
    --navy: #0f2c5c;
    --ink-blue: #1c3f7a;
    --icon-blue: #3b7fd0;
    --frame-grey: #c4c4c4;
    --arrow-grey: #c9c9c9;
  }
  html, body {
    margin: 0;
    padding: 0;
    width: 1200px;
    height: 1000px;
    overflow: hidden;
    background: var(--backdrop);
    font-family: "Questrial", "Century Gothic", sans-serif;
  }
  .stage {
    position: relative;
    width: 1200px;
    height: 1000px;
  }
  .label {
    position: absolute;
    background: var(--label-paper);
    box-shadow: 2px 3px 6px rgba(0,0,0,0.45);
  }
  .label--wide { left: 115px; top: 300px; width: 467px; height: 388px; }
  .label--tall { left: 703px; top: 300px; width: 388px; height: 467px; }

  .brand {
    position: absolute;
    display: flex;
    align-items: center;
    gap: 14px;
  }
  .brand__name {
    color: var(--navy);
    font-size: 25px;
    letter-spacing: 0.14em;
    text-transform: uppercase;
    line-height: 1.15;
    white-space: nowrap;
  }
  .brand__dot {
    width: 52px;
    height: 52px;
    border-radius: 50%;
    background: var(--ink-blue);
    flex: none;
  }
  .label--wide .brand { left: 28px; top: 34px; }
  .label--tall .brand { left: 22px; top: 44px; }
  .label--tall .brand__name { font-size: 20px; }
  .label--tall .brand__dot { width: 48px; height: 48px; }

  .sender {
    position: absolute;
    color: var(--ink-blue);
    font-size: 14px;
    line-height: 20px;
  }
  .label--wide .sender { left: 27px; top: 117px; }
  .label--tall .sender { left: 20px; top: 128px; }
  .sender__lines { display: flex; gap: 20px; }
  .sender__item { display: flex; align-items: center; gap: 8px; }
  .sender__item svg { width: 14px; height: 14px; }

  .address-box {
    position: absolute;
    border: 2px solid var(--frame-grey);
    box-sizing: border-box;
  }
  .label--wide .address-box { left: 28px; top: 187px; width: 411px; height: 174px; }
  .label--tall .address-box { left: 22px; top: 201px; width: 344px; height: 242px; }
  .address-box svg { position: absolute; left: -2px; top: 0; height: 100%; }
</style>
</head>
<body>
<main class="stage">

  <section class="label label--wide">
    <div class="brand">
      <span class="brand__name">Marrick<br>Global Logistics</span>
      <span class="brand__dot"></span>
    </div>
    <div class="sender">
      <div>58 Harbour Lane, Eastwick, NSW 2049</div>
      <div class="sender__lines">
        <span class="sender__item">
          <svg viewBox="0 0 14 14"><circle cx="7" cy="7" r="6.2" fill="none" stroke="var(--icon-blue)" stroke-width="1.2"/><path d="M4.6 3.8c-.6.4-.7 1.4 0 2.8s2 2.9 3.3 3.4c1 .4 1.7.1 2-.5l-1.3-1.1-.8.6c-.7-.3-1.7-1.3-2-2l.6-.8L5.4 3.6z" fill="var(--icon-blue)"/></svg>
          02 8100 4400
        </span>
        <span class="sender__item">
          <svg viewBox="0 0 14 14"><circle cx="7" cy="7" r="6.2" fill="none" stroke="var(--icon-blue)" stroke-width="1.2"/><rect x="4.5" y="3.5" width="5" height="2.5" fill="var(--icon-blue)"/><rect x="3.3" y="6.2" width="7.4" height="3.2" rx=".6" fill="var(--icon-blue)"/><rect x="4.5" y="8.6" width="5" height="2" fill="var(--label-paper)" stroke="var(--icon-blue)" stroke-width=".6"/></svg>
          02 9100 4411
        </span>
      </div>
    </div>
    <div class="address-box">
      <svg viewBox="0 0 34 174" width="34" preserveAspectRatio="none"><polygon points="0,6 32,87 0,168" fill="var(--arrow-grey)"/></svg>
    </div>
  </section>

  <section class="label label--tall">
    <div class="brand">
      <span class="brand__name">Marrick<br>Global Logistics</span>
      <span class="brand__dot"></span>
    </div>
    <div class="sender">
      <div>58 Harbour Lane, Eastwick, NSW 2049</div>
      <div class="sender__lines">
        <span class="sender__item">
          <svg viewBox="0 0 14 14"><circle cx="7" cy="7" r="6.2" fill="none" stroke="var(--icon-blue)" stroke-width="1.2"/><path d="M4.6 3.8c-.6.4-.7 1.4 0 2.8s2 2.9 3.3 3.4c1 .4 1.7.1 2-.5l-1.3-1.1-.8.6c-.7-.3-1.7-1.3-2-2l.6-.8L5.4 3.6z" fill="var(--icon-blue)"/></svg>
          02 8100 4400
        </span>
        <span class="sender__item">
          <svg viewBox="0 0 14 14"><circle cx="7" cy="7" r="6.2" fill="none" stroke="var(--icon-blue)" stroke-width="1.2"/><rect x="4.5" y="3.5" width="5" height="2.5" fill="var(--icon-blue)"/><rect x="3.3" y="6.2" width="7.4" height="3.2" rx=".6" fill="var(--icon-blue)"/><rect x="4.5" y="8.6" width="5" height="2" fill="var(--label-paper)" stroke="var(--icon-blue)" stroke-width=".6"/></svg>
          02 9100 4411
        </span>
      </div>
    </div>
    <div class="address-box">
      <svg viewBox="0 0 44 242" width="44" preserveAspectRatio="none"><polygon points="0,14 42,121 0,228" fill="var(--arrow-grey)"/></svg>
    </div>
  </section>

</main>
</body>
</html>
```